Business Cards Needed for Innovative Healthcare Marketing Company

We are a marketing company focused on healthcare. Our company is all about rebranding yourself renewing your image and generating results. The phoenix stands for "reborn" or "rising" which we provide new brands for our clients we take their old brands and renew it with creativity and innovation. I am looking for a business card with color dimension. I have attached an example of a card I think has the look and feel of what I am trying to accomplish. I like that the card example has black and grey font colors, I like the font placement and the small logo, I really like the use of the colors on the right those are the colors of my logo. My logo is phoenix so maybe incorporating flames similar to that design. I would like the back a solid color maybe red with an opaque version of the logo and website. As a marketing company I am always open to creative liberty!

Target Market(s)

Doctors and business professionals.

Industry/Entity Type

Marketing

Contact Information for Business Card

Vornaly Health Care Marketing
Marnie Okonski- CEO
#(502)638-2947
email-marnie@vornaly.com
website- vornaly.com

Font styles to use
Sans Serif

Colors
ec1f27
f37122
ffc214
fbed22
fbf289
f04a50

Requirements
Must have
• The logo and required information
Nice to have
• icons by the information
Should not have
• child like font

```html
<!DOCTYPE html>
<html lang="en">
<head>
<meta charset="utf-8">
<title>Vornaly Health Care Marketing – Business Card</title>
<link rel="stylesheet" href="https://fonts.googleapis.com/css2?family=Lato:wght@300;400;700&display=swap">
<style>
  :root {
    --stage: #2c2c2e;
    --paper: #ffffff;
    --brand-red: #ec1f27;
    --brand-deep: #a3261f;
    --flame-top: #dc6c26;
    --flame-bottom: #f0922a;
    --back-red: #eb2228;
    --back-flame: #d8242a;
    --ink: #111111;
    --ink-soft: #2a2a2a;
  }
  * { margin: 0; padding: 0; box-sizing: border-box; }
  html, body {
    width: 1200px; height: 900px; overflow: hidden;
    background: var(--stage);
    font-family: "Lato", sans-serif;
  }
  .card {
    position: absolute; left: 293px; width: 611px; height: 357px; overflow: hidden;
  }
  .card--front { top: 74px; background: var(--paper); }
  .card--back { top: 470px; background: var(--back-red); }

  .flame-art {
    position: absolute; right: 0; top: 0; width: 305px; height: 100%;
  }
  .card--front .flame-art {
    background: linear-gradient(180deg, var(--flame-top), var(--flame-bottom));
    border-top-left-radius: 180px 357px;
  }
  .card--back .flame-art {
    right: 0; width: 250px;
    background: linear-gradient(180deg, var(--back-flame), rgba(216,36,42,0.6));
    border-top-left-radius: 160px 357px;
  }

  .brand {
    position: absolute; left: 38px; top: 60px;
    display: flex; align-items: center; gap: 12px;
    color: var(--brand-deep); font-weight: 300;
  }
  .brand__dot { width: 58px; height: 58px; border-radius: 50%; background: var(--brand-deep); }
  .brand__name { font-size: 40px; letter-spacing: 1px; line-height: 1; }
  .brand__tag {
    font-size: 13px; letter-spacing: 0.8px; margin-top: 6px;
    padding-top: 5px; border-top: 1px solid var(--brand-deep);
  }

  .contact { position: absolute; left: 39px; top: 232px; color: var(--ink-soft); }
  .contact__name { font-size: 15px; font-weight: 700; color: var(--ink); margin-bottom: 14px; }
  .contact__role { color: var(--brand-red); }
  .contact__list { list-style: none; font-size: 13px; }
  .contact__list li { display: flex; align-items: center; gap: 7px; height: 19px; }
  .contact__icon { width: 12px; height: 12px; flex: none; }

  .back-brand {
    position: absolute; left: 0; right: 0; top: 208px;
    text-align: center; color: #ffffff; font-weight: 300;
  }
  .back-brand__name { font-size: 46px; letter-spacing: 1px; line-height: 1; }
  .back-brand__tag {
    display: inline-block; font-size: 14px; letter-spacing: 1px;
    margin-top: 6px; padding-top: 5px; border-top: 1px solid #ffffff;
  }
  .back-url {
    position: absolute; left: 0; right: 0; top: 314px;
    text-align: center; color: #ffffff; font-size: 13px; font-weight: 400;
  }
</style>
</head>
<body>

<section class="card card--front">
  <div class="brand">
    <span class="brand__dot"></span>
    <div>
      <div class="brand__name">VORNALY</div>
      <div class="brand__tag">HEALTH CARE MARKETING</div>
    </div>
  </div>

  <div class="contact">
    <p class="contact__name">Marnie Okonski-<span class="contact__role">CEO</span></p>
    <ul class="contact__list">
      <li>
        <svg class="contact__icon" viewBox="0 0 12 12"><rect width="12" height="12" rx="2" fill="#ec1f27"/><path d="M3.5 2.8l1.4 1.5-.7 1c.5 1 1.3 1.8 2.3 2.3l1-.7 1.5 1.4-.9 1.2C5.6 9.3 2.7 6.4 2.5 3.7z" fill="#fff"/></svg>
        #(502)638-2947
      </li>
      <li>
        <svg class="contact__icon" viewBox="0 0 12 12"><rect width="12" height="12" rx="2" fill="#ec1f27"/><rect x="2.5" y="3.5" width="7" height="5" fill="none" stroke="#fff" stroke-width="1"/><path d="M2.5 3.5L6 6.3 9.5 3.5" fill="none" stroke="#fff" stroke-width="1"/></svg>
        marnie@vornaly.com
      </li>
      <li>
        <svg class="contact__icon" viewBox="0 0 12 12"><rect width="12" height="12" rx="2" fill="#ec1f27"/><rect x="2.5" y="3" width="7" height="4.5" fill="none" stroke="#fff" stroke-width="1"/><path d="M4.5 9h3" stroke="#fff" stroke-width="1"/></svg>
        vornaly.com
      </li>
    </ul>
  </div>

  <div class="flame-art" role="img" aria-label="Orange flame illustration rising along the right edge"></div>
</section>

<section class="card card--back">
  <div class="flame-art" role="img" aria-label="Faint red flame illustration along the right side"></div>
  <div class="back-brand">
    <div class="back-brand__name">VORNALY</div>
    <div class="back-brand__tag">HEALTH CARE MARKETING</div>
  </div>
  <p class="back-url">www.vornaly.com</p>
</section>

</body>
</html>
```